New shirt company looking for a fun and edgy online retail website design

We're a new company looking for a simple yet attractive website to sell shirts/tops to a mostly younger female audience. Our name is Tavi Shirt Co. and the PlanHerd logo is uploaded. We're thinking a home page, three separate pages for our shirt "collections", and a contact page/cart page for a grand total of 5 pages. We'd like the website to be coded, easy for the consumer to navigate/shop/checkout, and easy to link to various social media platforms and online websites. For colors, we're aiming for various blues, light grey, and maybe tan/khaki. Our goal is to launch with approximately 20-30 tops/shirts (or 7-10) per page. Please let us know if you have any questions and thank you for helping us! We are very excited to see what is created!

Target Market(s)

Female teens to early twenties

Coding

Coded - Design and coding required

Number of Pages Required

3 page

Font styles to use
Decorative
Script

Colors
cee9f5
85cae6
33a6d7
0393ce
cfdfed
85acd3

Requirements
Must have
• Online shopping/purchasing capabilities, dropdowns to select sizes for each item, easy to add/remove new or seasoned items.

```html
<!DOCTYPE html>
<html lang="en">
<head>
<meta charset="utf-8">
<title>Tavi Shirt Co. — Your Cart</title>
<link rel="stylesheet" href="https://fonts.googleapis.com/css2?family=Montserrat:wght@400;500;600;700&display=swap">
<style>
:root{
  --blue:#0393ce;
  --sky:#85cae6;
  --panel:#cee6f3;
  --ink:#333;
  --red:#b23440;
  --footer:#222;
  --footer-deep:#151515;
  --tile:#333;
  --white:#fff;
}
*{box-sizing:border-box;margin:0;padding:0}
html,body{width:1200px;height:2577px;overflow:hidden}
body{position:relative;font-family:'Montserrat',sans-serif;background:#fff;color:var(--ink)}
.abs{position:absolute}
.brand-box{background:var(--sky);display:flex;align-items:center;justify-content:center;color:var(--blue);font-weight:700}
.site-logo{left:63px;top:0;width:205px;height:105px;font-size:20px}
.nav{left:516px;top:46px;display:flex;gap:42px;font-size:15px;font-weight:500;text-transform:uppercase}
.nav a{color:var(--ink);text-decoration:none}
.nav a.active{color:var(--blue)}
.round-btn{width:42px;height:42px;border-radius:50%;background:var(--blue);top:35px}
.page-title{left:0;width:1200px;top:348px;text-align:center;font-size:42px;font-weight:600;color:var(--blue)}
.cart-item{left:66px;width:1069px;height:428px;background:var(--panel)}
.cart-item h2{position:absolute;left:51px;top:28px;font-size:26px;font-weight:700}
.photo{position:absolute;left:52px;top:78px;width:311px;height:310px;border-radius:12px}
.details{position:absolute;left:421px;top:100px;color:var(--blue)}
.label{font-size:21px;font-weight:700}
.price{margin-top:18px;font-size:20px}
.price s,.save{font-weight:700}
.save{text-decoration:line-through;font-size:20px;margin-top:20px;display:block}
.btn{display:flex;align-items:center;justify-content:center;gap:10px;height:55px;width:228px;color:var(--white);font-size:14px;font-weight:600;text-transform:uppercase}
.btn-primary{background:var(--blue)}
.btn-danger{background:var(--red)}
.actions{position:absolute;left:423px;top:306px;display:flex;gap:30px}
.summary{left:66px;top:1411px;width:1069px;height:493px;background:var(--panel)}
.summary h2{text-align:center;font-size:26px;font-weight:700;margin-top:28px}
.row{position:absolute;left:115px;width:838px;height:92px;border-bottom:2px solid #fff;font-size:20px}
.row .col{position:absolute;top:0}
.row .k{color:var(--blue);margin-bottom:8px}
.total{position:absolute;left:115px;width:838px;top:290px;height:80px;border-bottom:2px solid #fff;text-align:center;font-size:20px}
.up{left:570px;top:1960px;width:60px;height:60px;border-radius:50%;background:var(--blue);z-index:2;display:flex;align-items:center;justify-content:center}
.footer{left:0;top:1990px;width:1200px;height:465px;background:var(--footer);color:var(--white)}
.footer-logo{left:233px;top:111px;width:145px;height:83px;font-size:15px}
.contact{display:flex;align-items:center;gap:18px;font-size:26px;font-weight:600}
.ring{width:54px;height:54px;border:2px solid #fff;border-radius:50%;display:flex;align-items:center;justify-content:center}
.links h3{font-size:24px;font-weight:500;margin-bottom:12px}
.links a{display:flex;align-items:center;width:202px;height:43px;background:var(--tile);padding-left:24px;color:var(--white);text-decoration:none;font-size:15px;font-weight:500;margin-bottom:25px}
.bottom{left:0;top:2455px;width:1200px;height:122px;background:var(--footer-deep);color:var(--white)}
.copy{left:64px;top:44px;font-size:16px}
.pay{top:34px;width:64px;height:40px;background:#fff;border-radius:3px;display:flex;align-items:center;justify-content:center;font-size:10px;font-weight:700;color:var(--ink)}
</style>
</head>
<body>

<header>
  <div class="abs brand-box site-logo">Tavi Shirt Co.</div>
  <nav class="abs nav">
    <a class="active" href="#">Home</a><a href="#">About Us</a><a href="#">Collections</a><a href="#">Contact Us</a>
  </nav>
  <div class="abs round-btn" style="left:1029px">
    <svg width="42" height="42" viewBox="0 0 42 42"><path d="M13 14h3l3 10h9l2-7H17" fill="none" stroke="#fff" stroke-width="2.5"/><circle cx="20" cy="28" r="1.8" fill="#fff"/><circle cx="27" cy="28" r="1.8" fill="#fff"/></svg>
  </div>
  <div class="abs round-btn" style="left:1094px">
    <svg width="42" height="42" viewBox="0 0 42 42"><circle cx="21" cy="17" r="5" fill="#fff"/><path d="M12 29c1-6 17-6 18 0z" fill="#fff"/></svg>
  </div>
</header>

<svg class="abs" style="left:555px;top:255px" width="90" height="86" viewBox="0 0 90 86">
  <path d="M0 0h18l8 16h64l-12 40H28L14 8H0z" fill="#0393ce"/>
  <circle cx="32" cy="75" r="10" fill="#0393ce"/><circle cx="69" cy="75" r="10" fill="#0393ce"/>
</svg>
<h1 class="abs page-title">YOUR CART</h1>

<section class="abs cart-item" style="top:485px">
  <h2>Tavi's net sleeves &nbsp;black top beige colored 100% cotton #344453</h2>
  <div class="photo" role="img" aria-label="Model wearing a beige off-shoulder knit top" style="background:linear-gradient(180deg,#f4f1ee,#c9b9a8 60%,#6a7f97)"></div>
  <div class="details">
    <div class="label">Item Price:</div>
    <div class="price"><s>$30</s> <b>$25</b>&nbsp; 30%off</div>
    <div class="label" style="margin-top:34px">Your savings:</div>
    <span class="save">You Save :$5</span>
  </div>
  <div class="actions">
    <div class="btn btn-primary">Proceed to check out</div>
    <div class="btn btn-danger"><svg width="16" height="18" viewBox="0 0 16 18"><path d="M1 3h14M6 1h4M3 5l1 12h8l1-12" fill="none" stroke="#fff" stroke-width="2"/></svg>Remove from cart</div>
  </div>
</section>

<section class="abs cart-item" style="top:948px">
  <h2>Tavi's net sleeves &nbsp;white top white colored 100% cotton #349853</h2>
  <div class="photo" role="img" aria-label="Model wearing a white wrap blouse over a black top" style="background:linear-gradient(180deg,#f3f4f6,#dfe6ec 55%,#2a2a2a)"></div>
  <div class="details">
    <div class="label">Item Price:</div>
    <div class="price"><s>$30</s> <b>$25</b>&nbsp; 30%off</div>
    <div class="label" style="margin-top:34px">Your savings:</div>
    <span class="save">You Save :$5</span>
  </div>
  <div class="actions">
    <div class="btn btn-primary">Proceed to check out</div>
    <div class="btn btn-danger"><svg width="16" height="18" viewBox="0 0 16 18"><path d="M1 3h14M6 1h4M3 5l1 12h8l1-12" fill="none" stroke="#fff" stroke-width="2"/></svg>Remove from cart</div>
  </div>
</section>

<section class="abs summary">
  <h2>Check Out All Items</h2>
  <div class="row" style="top:93px">
    <div class="col" style="left:44px"><div class="k">Item Name:</div>Tavis Net Sleeves White top(349853)</div>
    <div class="col" style="left:562px"><div class="k">Item Price:</div>$25 + $5 delivery &amp; tax</div>
  </div>
  <div class="row" style="top:185px">
    <div class="col" style="left:44px;top:8px"><div class="k">Item Name:</div>Tavis Net Sleeves White top(349853)</div>
    <div class="col" style="left:562px;top:8px"><div class="k">Item Price:</div>$25 + $5 delivery &amp; tax</div>
  </div>
  <div class="total"><div style="color:var(--blue);margin:3px 0 8px">Grand Total:</div>$60 only</div>
  <div class="btn btn-primary" style="position:absolute;left:421px;top:406px">Proceed to check out</div>
</section>

<div class="abs up"><svg width="28" height="18" viewBox="0 0 28 18"><path d="M3 15L14 4l11 11" fill="none" stroke="#fff" stroke-width="4"/></svg></div>

<footer class="abs footer">
  <div class="abs brand-box footer-logo">Tavi Shirt Co.</div>
  <div class="abs contact" style="left:170px;top:237px">
    <div class="ring"><svg width="22" height="22" viewBox="0 0 24 24"><path d="M6.6 10.8a15 15 0 006.6 6.6l2.2-2.2a1 1 0 011-.25 11 11 0 003.6.6 1 1 0 011 1V20a1 1 0 01-1 1A17 17 0 013 4a1 1 0 011-1h3.5a1 1 0 011 1 11 11 0 00.6 3.6 1 1 0 01-.25 1z" fill="#fff"/></svg></div>
    5550 2468 1010
  </div>
  <div class="abs contact" style="left:112px;top:329px">
    <div class="ring"><svg width="22" height="16" viewBox="0 0 22 16"><rect width="22" height="16" rx="2" fill="#fff"/><path d="M1 1l10 8 10-8" fill="none" stroke="#222" stroke-width="2"/></svg></div>
    hello@tavishirt.com
  </div>
  <div class="abs links" style="left:588px;top:100px">
    <h3>EXPLORE</h3>
    <a href="#">WINTER SPECIALE</a><a href="#">COLLECTION NAME</a><a href="#">THE COLLECTIONS</a><a href="#">MY CART</a>
  </div>
  <div class="abs links" style="left:884px;top:100px">
    <h3>SITEMAP</h3>
    <a href="#">HOME</a><a href="#">COLLECTIONS</a><a href="#">PRODUCTS</a><a href="#">CONTACT US</a>
  </div>
</footer>

<div class="abs bottom">
  <div class="abs copy">© Copyright Tavi Clothings &nbsp;pvt ltd</div>
  <div class="abs pay" style="left:708px">CardOne</div>
  <div class="abs pay" style="left:798px">WireSend</div>
  <div class="abs pay" style="left:889px">ExpressPay</div>
  <div class="abs pay" style="left:979px">MeshCard</div>
  <div class="abs pay" style="left:1069px">PayPost</div>
</div>

</body>
</html>
```